Website for company called VORENTbio

We need a website for our new company called VORENTbio which developed a platform/technology to identify antigen-specific T cells (immune cells) which can be used for cancer therapy, autoimmunity, etc.

The platform is called VORENT and is rapid, versatile, unbiased, and inexpensive.

We have a semi-final logo although we are not completely set on color and font of text (attached).

Target Market(s)

Our target audience at the moment would be potential investors and VCs. We eventually are interested in getting attention from scientists and cell/immunotherapy companies.

Industry/Entity Type

Healthcare/Technology

Coding

Coded - Design and coding required

Number of Pages Required

1 page

Colors
0094D4
00A9DD
6FCCEA
C7EBF8
E9F6FB
00AB8E
00BBA5
67D7C9
C6EFE9
E9F9F6
E54698
E96AAD
F1A4CE
F9D9EA
FCEFF6
A7469A
B969AE
D3A5CF
EDDBEB
F8F0F9
6B429C
8869AF
B7A5CE
E3DAEB
F3F0F8

Requirements
Must have
• Landing page about the company, About us page, Technology page (could be merged with company landing page), Contact us page

```html
<!DOCTYPE html>
<html lang="en">
<head>
<meta charset="utf-8">
<title>VORENTbio — Precision Immune Targeting</title>
<link href="https://fonts.googleapis.com/css2?family=Sora:wght@400;600;700;800&family=Plus+Jakarta+Sans:wght@400;500;600;700&display=swap" rel="stylesheet">
<style>
:root{
  --page:#eef2fb;
  --white:#ffffff;
  --navy:#0a1947;
  --blue:#3561f0;
  --ink:#10163a;
  --muted:#6b7188;
  --line:#d7dcea;
  --outline:#b9c0d6;
  --head:'Sora',sans-serif;
  --body:'Plus Jakarta Sans',sans-serif;
}
*{box-sizing:border-box;margin:0;padding:0}
html,body{width:1200px;height:4219px;overflow:hidden}
body{background:var(--page);font-family:var(--body);color:var(--ink);position:relative}
.abs{position:absolute}

/* header */
.brand{left:44px;top:28px;font-family:var(--head);font-weight:700;font-size:30px;color:var(--ink);display:flex;align-items:center;gap:10px;letter-spacing:-.5px}
.brand-dot{width:18px;height:18px;border-radius:50%;background:var(--ink)}
.nav{left:542px;top:25px;width:401px;height:44px;background:var(--white);border-radius:22px;display:flex;align-items:center;justify-content:center;gap:18px;font-size:11px;font-weight:600;letter-spacing:.3px}
.nav a{color:var(--ink);text-decoration:none}
.nav a.active{color:var(--blue)}
.nav .sep{width:4px;height:4px;border-radius:50%;background:var(--blue)}
.search{left:964px;top:37px}
.cta{left:1002px;top:26px;width:152px;height:43px;border-radius:22px;background:var(--blue);color:#fff;font-size:9.5px;font-weight:700;display:flex;align-items:center;justify-content:center;letter-spacing:.2px}

/* hero */
.hero{left:44px;top:95px;width:1110px;height:561px;border-radius:18px;overflow:hidden;background:linear-gradient(115deg,#1a2fa0 0%,#1f55c8 45%,#2b86cf 75%,#2f9bcf 100%)}
.hero-title{left:118px;top:220px;font-family:var(--head);font-weight:800;font-size:74px;line-height:66px;color:#fff;letter-spacing:-.5px}
.hero-sub{left:121px;top:360px;font-family:var(--head);font-weight:600;font-size:30px;color:#fff}
.hero-text{left:120px;top:440px;font-size:14px;color:#fff}
.hero-btn{left:120px;top:481px;width:176px;height:43px;border-radius:22px;background:#fff;font-size:9px;font-weight:700;display:flex;align-items:center;justify-content:center;color:var(--ink)}
.hero-arrow{width:60px;height:60px;border-radius:50%;display:flex;align-items:center;justify-content:center}
.hero-arrow.prev{left:1003px;top:561px;background:rgba(255,255,255,.18);border:1px solid rgba(255,255,255,.5)}
.hero-arrow.next{left:1069px;top:561px;background:#fff}

/* marquee */
.marquee{left:-8px;top:692px;font-family:var(--head);font-weight:800;font-size:78px;white-space:nowrap;color:transparent;-webkit-text-stroke:1.5px var(--outline);letter-spacing:1px}

/* about */
.card{background:var(--white);border-radius:18px}
.about{left:44px;top:825px;width:1108px;height:606px}
.cell-visual{left:222px;top:884px;width:368px;height:344px;border-radius:20px;background:linear-gradient(150deg,#eef0fa 0%,#c9cdee 45%,#8d95d2 100%)}
.h2{font-family:var(--head);font-weight:700;font-size:28px;letter-spacing:-.3px;color:var(--ink)}
.about-h{left:629px;top:934px}
.about-p{left:629px;top:983px;width:350px;font-size:11.5px;line-height:19px;color:var(--muted)}
.about-m{left:629px;top:1081px;font-size:11px;font-weight:700}
.about-m2{left:629px;top:1106px;width:350px;font-size:11.5px;line-height:19px;color:var(--muted)}
.about-rule{left:157px;top:1264px;width:884px;height:1px;background:var(--line)}
.stat{top:1300px}
.stat-num{font-family:var(--head);font-weight:700;font-size:60px;line-height:62px;color:transparent;-webkit-text-stroke:1.5px var(--outline);letter-spacing:-1px}
.stat-label{font-size:11px;font-weight:700;margin-top:16px;letter-spacing:.2px}

/* how it works */
.how-h{left:147px;top:1535px}
.how-rule{left:417px;top:1552px;width:618px;height:1px;background:var(--line)}
.step{top:1608px;width:200px}
.step-icon{width:74px;height:74px;border-radius:50%;background:var(--blue);display:flex;align-items:center;justify-content:center;margin-left:1px}
.step-title{font-size:11px;font-weight:700;margin-top:27px;letter-spacing:.2px}
.step-text{font-size:11.5px;line-height:19px;color:var(--muted);margin-top:12px;width:160px}

/* intro */
.intro{left:44px;top:1884px;width:1108px;height:547px;border-radius:18px;background:var(--navy);overflow:hidden}
.intro-h{left:188px;top:2036px;color:#fff}
.intro-p{left:188px;top:2087px;width:345px;font-size:11.5px;line-height:18.5px;color:#d6dcf2}
.gauge{top:2210px;display:flex;align-items:center;gap:14px}
.gauge-ring{width:88px;height:88px;border-radius:50%;border:3px solid #2f59e8;border-left-color:#fff;border-bottom-color:#fff;display:flex;align-items:center;justify-content:center;background:var(--navy)}
.gauge-ring span{width:64px;height:64px;border-radius:50%;background:#fff;color:var(--ink);font-family:var(--head);font-weight:600;font-size:18px;display:flex;align-items:center;justify-content:center}
.gauge-ring sup{font-size:8px}
.gauge-label{font-size:9px;font-weight:700;color:#fff;line-height:14px}
.flask-visual{left:647px;top:1948px;width:368px;height:410px;border-radius:20px;background:radial-gradient(ellipse at 50% 65%,rgba(80,120,255,.5),rgba(30,60,170,.22) 50%,rgba(10,25,71,0) 75%)}

/* why */
.why-h{left:0;top:2530px;width:1200px;text-align:center}
.row{left:154px;width:892px;height:104px;border-bottom:1px solid var(--line)}
.row-num{position:absolute;left:37px;font-family:var(--head);font-weight:700;font-size:44px;color:transparent;-webkit-text-stroke:1.3px var(--outline)}
.row-title{position:absolute;left:185px;font-size:11px;font-weight:700;line-height:19px;width:220px}
.row-text{position:absolute;left:473px;font-size:11.5px;line-height:19px;color:var(--muted);width:280px}
.row-arrow{position:absolute;left:833px}

/* applications */
.apps-h{left:43px;top:3118px;font-size:30px}
.app{top:3184px;width:264px;height:331px;border-radius:16px;overflow:hidden}
.app-label{position:absolute;left:33px;bottom:31px;background:#fff;border-radius:5px;padding:10px 14px;font-size:9.5px;font-weight:700;line-height:12px;min-width:168px}
.dots{left:582px;top:3549px;display:flex;gap:7px}
.dots i{width:6px;height:6px;border-radius:50%;background:var(--ink)}
.dots i.on{background:var(--blue)}

/* footer */
.footer{left:44px;top:3669px;width:1108px;height:560px;border-radius:18px 18px 0 0;background:var(--navy)}
.f-brand{left:112px;top:3848px;font-family:var(--head);font-weight:700;font-size:46px;color:#fff;display:flex;align-items:center;gap:12px}
.f-brand i{width:20px;height:20px;border-radius:50%;background:#fff}
.social{top:3962px;width:40px;height:40px;border-radius:50%;border:1px solid rgba(255,255,255,.35)}
.sub-h{left:449px;top:3764px;color:#fff;font-size:28px;line-height:32px}
.sub-form{left:796px;top:3769px;width:288px;height:48px;border-radius:24px;background:#fff;display:flex;align-items:center}
.sub-form span{font-size:10.5px;color:var(--muted);padding-left:22px;flex:1}
.sub-form b{width:106px;height:48px;border-radius:24px;background:var(--blue);color:#fff;font-size:11.5px;display:flex;align-items:center;justify-content:center}
.f-rule{left:449px;top:3873px;width:631px;height:1px;background:rgba(255,255,255,.25)}
.f-col{top:3940px;font-size:11px;line-height:22.5px;color:#dfe4f5}
.f-contact-h{left:918px;top:3930px;font-family:var(--head);font-weight:700;font-size:15px;color:#fff}
.f-contact{left:918px;top:3958px;font-size:11px;line-height:22.5px;color:#fff}
.bar{left:218px;top:4157px;width:758px;height:62px;border-radius:22px 22px 0 0;background:#fff;font-size:10.5px;color:var(--ink)}
.bar .copy{position:absolute;left:31px;top:26px}
.bar .legal{position:absolute;left:535px;top:26px}
.up{left:1044px;top:4157px;width:36px;height:36px;border-radius:50%;background:var(--blue);display:flex;align-items:center;justify-content:center}
</style>
</head>
<body>

<!-- header -->
<div class="abs brand"><span class="brand-dot"></span>vorentbio</div>
<nav class="abs nav">
  <a class="active" href="#">HOME</a><span class="sep"></span>
  <a href="#">ABOUT</a><span class="sep"></span>
  <a href="#">TECHNOLOGY</a><span class="sep"></span>
  <a href="#">CONTACT</a>
</nav>
<svg class="abs search" width="18" height="18" viewBox="0 0 18 18"><circle cx="7.5" cy="7.5" r="5.2" fill="none" stroke="#10163a" stroke-width="1.6"/><line x1="11.5" y1="11.5" x2="15" y2="15" stroke="#10163a" stroke-width="1.6" stroke-linecap="round"/></svg>
<div class="abs cta">GET IN TOUCH WITH US</div>

<!-- hero -->
<section class="abs hero" role="img" aria-label="Microscopic scene of blue DNA strands and orange immune cells"></section>
<h1 class="abs hero-title">PRECISION<br>IMMUNE</h1>
<div class="abs hero-sub">TARGETING STARTS HERE</div>
<p class="abs hero-text">Discover VORENT — a rapid, versatile, and affordable platform</p>
<div class="abs hero-btn">LEARN HOW VORENT WORKS</div>
<div class="abs hero-arrow prev"><svg width="20" height="14" viewBox="0 0 20 14"><path d="M19 7H2M7 1L1 7l6 6" fill="none" stroke="#fff" stroke-width="1.6"/></svg></div>
<div class="abs hero-arrow next"><svg width="20" height="14" viewBox="0 0 20 14"><path d="M1 7h17M13 1l6 6-6 6" fill="none" stroke="#10163a" stroke-width="1.6"/></svg></div>

<div class="abs marquee">CIENTIFIC &nbsp;+&nbsp; RESEARCH &nbsp;+&nbsp; IMMUNOLOGY</div>

<!-- about -->
<section class="abs card about"></section>
<div class="abs cell-visual" role="img" aria-label="Close-up rendering of a purple-blue immune cell"></div>
<h2 class="abs h2 about-h">ABOUT VORENTBIO</h2>
<p class="abs about-p">Founded by scientists and driven by innovation, VORENTbio is advancing the future of immune diagnostics. Our mission is to accelerate the discovery of therapeutic T cells and support breakthroughs in personalized medicine.</p>
<div class="abs about-m">MISSION STATEMENT</div>
<p class="abs about-m2">To make immune profiling faster, smarter, and accessible for everyone developing the next generation of therapies.</p>
<div class="abs about-rule"></div>
<div class="abs stat" style="left:157px"><div class="stat-num">250+</div><div class="stat-label">SCIENTIFIC INTEGRITY</div></div>
<div class="abs stat" style="left:424px"><div class="stat-num">14m</div><div class="stat-label">REAL-WORLD IMPACT</div></div>
<div class="abs stat" style="left:656px"><div class="stat-num">430+</div><div class="stat-label">SPEED &amp; SIMPLICITY</div></div>
<div class="abs stat" style="left:922px"><div class="stat-num">30k</div><div class="stat-label">COLLABORATION</div></div>

<!-- how it works -->
<h2 class="abs h2 how-h">HOW IT WORKS</h2>
<div class="abs how-rule"></div>
<div class="abs step" style="left:149px">
  <div class="step-icon"><svg width="34" height="34" viewBox="0 0 34 34" fill="none" stroke="#fff" stroke-width="1.5"><circle cx="17" cy="17" r="6"/><path d="M17 3v8M17 23v8M3 17h8M23 17h8M7 7l5 5M22 22l5 5M27 7l-5 5M12 22l-5 5"/></svg></div>
  <div class="step-title">ISOLATE IMMUNE CELLS</div>
  <p class="step-text">Our clinical pathologists are available seven days a week to render diagnoses.</p>
</div>
<div class="abs step" style="left:393px">
  <div class="step-icon"><svg width="34" height="34" viewBox="0 0 34 34" fill="none" stroke="#fff" stroke-width="1.5"><circle cx="17" cy="17" r="14"/><circle cx="17" cy="17" r="8"/><path d="M11 11l12 12M23 11L11 23"/></svg></div>
  <div class="step-title">EXPOSE TO ANTIGENS</div>
  <p class="step-text">Our clinical pathologists are available seven days a week to render diagnoses.</p>
</div>
<div class="abs step" style="left:638px">
  <div class="step-icon"><svg width="34" height="34" viewBox="0 0 34 34" fill="none" stroke="#fff" stroke-width="1.5"><circle cx="17" cy="17" r="14"/><circle cx="17" cy="17" r="9"/><circle cx="17" cy="17" r="4"/></svg></div>
  <div class="step-title">DETECT ANTIGEN</div>
  <p class="step-text">Our clinical pathologists are available seven days a week to render diagnoses.</p>
</div>
<div class="abs step" style="left:882px">
  <div class="step-icon"><svg width="34" height="34" viewBox="0 0 34 34" fill="none" stroke="#fff" stroke-width="1.5"><rect x="6" y="5" width="22" height="25" rx="2"/><path d="M10 24l5-6 4 4 6-8"/><path d="M10 10h8"/></svg></div>
  <div class="step-title">ANALYZE RESULTS</div>
  <p class="step-text">Our clinical pathologists are available seven days a week to render diagnoses.</p>
</div>

<!-- introducing -->
<section class="abs intro"></section>
<div class="abs flask-visual" role="img" aria-label="Glowing blue laboratory flask surrounded by connected molecule points"></div>
<h2 class="abs h2 intro-h">INTRODUCING VORENT</h2>
<p class="abs intro-p">VORENT is a proprietary platform designed to identify antigen-specific T cells — the immune system's most targeted weapons. Our method is rapid, unbiased, and cost-effective, enabling new insights into immune response across cancer, autoimmune, and infectious diseases.</p>
<div class="abs gauge" style="left:186px"><div class="gauge-ring"><span>85<sup>%</sup></span></div><div class="gauge-label">TECHNOLOGIES<br>DEVELOPED</div></div>
<div class="abs gauge" style="left:388px"><div class="gauge-ring"><span>85<sup>%</sup></span></div><div class="gauge-label">HIGH END<br>TECHNOLOGY</div></div>

<!-- why different -->
<h2 class="abs h2 why-h">WHY IT’S DIFFERENT</h2>
<div class="abs row" style="top:2576px">
  <div class="row-num" style="top:28px">01.</div>
  <div class="row-title" style="top:33px">RAPID: SAME-DAY<br>INSIGHTS</div>
  <div class="row-text" style="top:33px">Our clinical pathologists are available seven days a week to render diagnoses.</div>
  <svg class="row-arrow" style="top:40px" width="18" height="18" viewBox="0 0 18 18" fill="none" stroke="#10163a" stroke-width="1.5"><path d="M3 15L15 3M6 3h9v9"/></svg>
</div>
<div class="abs row" style="top:2680px">
  <div class="row-num" style="top:28px">02.</div>
  <div class="row-title" style="top:33px">UNBIASED: NO NEED<br>FOR PREDEFINED MARKERS</div>
  <div class="row-text" style="top:33px">Our clinical pathologists are available seven days a week to render diagnoses.</div>
  <svg class="row-arrow" style="top:40px" width="18" height="18" viewBox="0 0 18 18" fill="none" stroke="#10163a" stroke-width="1.5"><path d="M3 15L15 3M6 3h9v9"/></svg>
</div>
<div class="abs row" style="top:2784px">
  <div class="row-num" style="top:28px">03.</div>
  <div class="row-title" style="top:33px">VERSATILE: WORKS ACROSS<br>DISEASES &amp; SAMPLE TYPES</div>
  <div class="row-text" style="top:33px">Our clinical pathologists are available seven days a week to render diagnoses.</div>
  <svg class="row-arrow" style="top:40px" width="18" height="18" viewBox="0 0 18 18" fill="none" stroke="#10163a" stroke-width="1.5"><path d="M3 15L15 3M6 3h9v9"/></svg>
</div>
<div class="abs row" style="top:2888px;height:121px">
  <div class="row-num" style="top:30px">04.</div>
  <div class="row-title" style="top:35px">AFFORDABLE: SCALES EASILY<br>IN BOTH RESEARCH &amp; CLINICAL<br>USE</div>
  <div class="row-text" style="top:35px">Our clinical pathologists are available seven days a week to render diagnoses.</div>
  <svg class="row-arrow" style="top:42px" width="18" height="18" viewBox="0 0 18 18" fill="none" stroke="#10163a" stroke-width="1.5"><path d="M3 15L15 3M6 3h9v9"/></svg>
</div>

<!-- applications -->
<h2 class="abs h2 apps-h">APPLICATIONS INCLUDE</h2>
<div class="abs app" style="left:44px;background:linear-gradient(160deg,#d9dde2,#b9a89a 60%,#8a8f9a)" role="img" aria-label="Doctor supporting a patient during treatment"><div class="app-label">CANCER IMMUNOTHERAPY<br>(CAR-T, TCR DISCOVERY)</div></div>
<div class="abs app" style="left:326px;background:linear-gradient(160deg,#e9d9d8,#c9a99c 55%,#a8887e)" role="img" aria-label="Woman holding her neck in discomfort"><div class="app-label">AUTOIMMUNE DISEASE<br>MONITORING</div></div>
<div class="abs app" style="left:607px;background:linear-gradient(160deg,#eef2f6,#c6d3e0 55%,#5f86c4)" role="img" aria-label="Lab technician in protective gear handling a test tube"><div class="app-label">INFECTIOUS DISEASE<br>RESPONSE</div></div>
<div class="abs app" style="left:889px;background:linear-gradient(160deg,#b48a78,#8d6a5e 50%,#2c5bc8)" role="img" aria-label="Gloved hands giving a vaccine injection in an arm"><div class="app-label">PERSONALIZED VACCINE<br>DEVELOPMENT</div></div>
<div class="abs dots"><i></i><i class="on"></i><i></i></div>

<!-- footer -->
<footer class="abs footer"></footer>
<div class="abs f-brand"><i></i>vorentbio</div>
<span class="abs social" style="left:141px"></span>
<span class="abs social" style="left:193px"></span>
<span class="abs social" style="left:245px"></span>
<span class="abs social" style="left:297px"></span>
<h2 class="abs h2 sub-h">SUBSCRIBE TO OUR<br>NEWSLETTER</h2>
<div class="abs sub-form"><span>Enter your email address</span><b>SUBMIT</b></div>
<div class="abs f-rule"></div>
<div class="abs f-col" style="left:449px">Home<br>About<br>Technology<br>Contact</div>
<div class="abs f-col" style="left:584px">Legal notices<br>Terms &amp; Condition<br>Privacy policy<br>Contact</div>
<div class="abs f-col" style="left:751px">Isolate Immune Cells<br>Expose to Antigens<br>Detect Antigen<br>Analyze Results</div>
<div class="abs f-contact-h">Contact Us</div>
<div class="abs f-contact">Some address line goes here<br>Mobile: +1 555 0142<br>Email: info@vorentbio.com</div>
<div class="abs bar"><span class="copy">Copyright © 2025 Vorentbio All Rights Reserved.</span><span class="legal">Privacy Policy &nbsp;|&nbsp; Terms and Condition</span></div>
<div class="abs up"><svg width="12" height="12" viewBox="0 0 12 12" fill="none" stroke="#fff" stroke-width="1.5"><path d="M6 11V1M2 5l4-4 4 4"/></svg></div>

</body>
</html>
```